CONTEMPORARY Canva Art Design for Christians

I need a canvas art design on Christianity. The design must be in 3 SIMPLE dimensions: 12x 18 inches / 28 x 24 inches / 30 x 40 inches
The design must be accompanied by christian quote.
The christian quote can be "As For Me And My House We Will Serve The Lord (Joshua 24:15)" or any other quote that is good for display in a christian home.

I DON'T WANT THE TRADITIONAL CHRISTIAN DESIGN.. I WANT COLOURFUL, MEANINGFUL and CONTEMPORARY, MODERN DESIGN. And stay away from the scary image of Jesus in dark background, it only makes the home more scary not holy!

Target Market(s)

Christians

Colors

Designer to choose colors to be used in the design.

Requirements
Must have
• A graphic design and a christian quote that is powerful and edifies the soul. Great for display at home. Great use of colours to enhance the message.
Nice to have
• I wish to see great unique design with strong use of colours, images to enhance the scripture. It must glorify Jesus.
Should not have
• Should not be dull.

```html
<!DOCTYPE html>
<html lang="en">
<head>
<meta charset="utf-8">
<title>As For Me And My House – Canvas Art</title>
<link href="https://fonts.googleapis.com/css2?family=Roboto+Condensed:wght@300&display=swap" rel="stylesheet">
<style>
  :root {
    --backdrop: #dcdcdc;
    --sky-night: #0c2b52;
    --sky-deep: #11558c;
    --sky-mid: #2f95cf;
    --sky-light: #6fc0e6;
    --horizon-glow: #f4f8fa;
    --field-light: #b3a26c;
    --field-dark: #6f6138;
    --road: #c9b88a;
    --text-white: #ffffff;
    --cross-glow: rgba(255, 255, 255, 0.85);
  }
  html, body {
    margin: 0;
    padding: 0;
    width: 1200px;
    height: 1200px;
    overflow: hidden;
    background: var(--backdrop);
  }
  .canvas {
    position: relative;
    width: 1200px;
    height: 1200px;
  }
  .print {
    position: absolute;
    left: 233px;
    top: 50px;
    width: 734px;
    height: 1100px;
    overflow: hidden;
    box-shadow: 0 4px 14px rgba(0,0,0,0.18);
  }
  .scene {
    position: absolute;
    inset: 0;
    background:
      radial-gradient(ellipse 260px 160px at 50% 75%, var(--horizon-glow) 0%, rgba(244,248,250,0) 100%),
      linear-gradient(to bottom,
        var(--sky-night) 0%,
        var(--sky-deep) 28%,
        var(--sky-mid) 50%,
        var(--sky-light) 64%,
        var(--horizon-glow) 74.5%,
        var(--field-light) 75%,
        var(--field-dark) 86%,
        var(--road) 100%);
  }
  .cross {
    position: absolute;
    inset: 0;
  }
  .quote {
    position: absolute;
    top: 62px;
    left: 0;
    width: 100%;
    margin: 0;
    text-align: center;
    color: var(--text-white);
    font-family: "Roboto Condensed", "Arial Narrow", sans-serif;
    font-weight: 300;
  }
  .quote__verse {
    display: block;
    font-size: 72px;
    line-height: 77px;
    letter-spacing: -0.5px;
  }
  .quote__reference {
    display: block;
    font-size: 38px;
    line-height: 44px;
    margin-top: -4px;
  }
</style>
</head>
<body>
<div class="canvas">
  <div class="print">
    <div class="scene" role="img" aria-label="Photograph of a starry blue sky fading to bright light at the horizon, a golden grass field and a dirt road with a traveller walking toward the light"></div>
    <svg class="cross" viewBox="0 0 734 1100" width="734" height="1100" aria-hidden="true">
      <defs>
        <filter id="glow" x="-50%" y="-50%" width="200%" height="200%">
          <feGaussianBlur stdDeviation="14"/>
        </filter>
      </defs>
      <g fill="var(--cross-glow)" filter="url(#glow)">
        <rect x="353" y="423" width="43" height="397"/>
        <rect x="246" y="514" width="257" height="42"/>
      </g>
      <g fill="#ffffff">
        <rect x="353" y="423" width="43" height="397"/>
        <rect x="246" y="514" width="257" height="42"/>
      </g>
    </svg>
    <h1 class="quote">
      <span class="quote__verse">AS FOR ME AND</span>
      <span class="quote__verse">MY HOUSE</span>
      <span class="quote__verse">WE WILL SERVE</span>
      <span class="quote__verse">THE LORD</span>
      <span class="quote__reference">(JOSHUA 24:15)</span>
    </h1>
  </div>
</div>
</body>
</html>
```